vorp business card design

vorp is an incubator within Qorvel Media focused on unlocking the potential in underserved niche micro-verticals on the web. our mission is to rapidly develop and foster emerging micro-verticals bc they are ripe for growth - building interesting and trusted content experiences with unqiue, useful and cutting-edge delivery methods.please do all copy (except for Qorvel Media, which must look as typed here and in logo) in all lowercase. Also please use spaces between phone # extensions not dashes or periods. I have attached all variations of the logo.
Industry/Entity Type
Business
Contact Information for Business Card
dale fenwright, ceo www.vorp.example 218 9th avenue 3rd floor lindenport ca 95555 415 602 0002m 510 985 7966d dale.fenwright@vorp.example
Look and feel

```html
<!DOCTYPE html>
<html lang="en">
<head>
<meta charset="utf-8">
<title>vorp business card</title>
<link rel="stylesheet" href="https://fonts.googleapis.com/css2?family=Source+Sans+3:wght@400;600&family=Didact+Gothic&display=swap">
<style>
  :root {
    --page: #e2e2e2;
    --ink: #111111;
    --paper-light: #ececec;
    --paper-dark: #cdcdcd;
    --band: #0a0a0a;
    --green: #229d71;
    --green-deep: #1b8e63;
    --white: #f2f2f2;
  }
  * { margin: 0; padding: 0; box-sizing: border-box; }
  html, body { width: 1189px; height: 1200px; overflow: hidden; background: var(--page); }
  .card {
    position: absolute; left: 134px; width: 920px; height: 522px; overflow: hidden;
    box-shadow: 0 6px 14px rgba(0,0,0,.35);
  }
  .card--front { top: 45px; }
  .card--back { top: 625px; background: var(--band); }

  .front-top {
    position: absolute; left: 0; top: 0; width: 100%; height: 277px;
    background: radial-gradient(ellipse at 60% 80%, var(--paper-light), var(--paper-dark));
  }
  .front-rule { position: absolute; left: 0; top: 277px; width: 100%; height: 25px; background: var(--band); }
  .front-info {
    position: absolute; left: 0; top: 302px; width: 100%; height: 220px;
    background: linear-gradient(180deg, var(--green-deep), var(--green));
  }

  .wordmark {
    position: absolute; font-family: "Source Sans 3", sans-serif; font-weight: 600;
    font-size: 200px; line-height: 1; letter-spacing: 4px;
  }
  .card--front .wordmark { left: 172px; top: 10px; color: var(--ink); }
  .card--back .wordmark { left: 212px; top: 114px; color: var(--white); }
  .mark-dot { position: absolute; width: 62px; height: 62px; border-radius: 50%; background: var(--green-deep); }
  .card--front .mark-dot { left: 654px; top: 120px; }
  .card--back .mark-dot { left: 664px; top: 226px; }

  .tagline { position: absolute; font-family: "Didact Gothic", sans-serif; font-size: 33px; white-space: nowrap; }
  .card--front .tagline { left: 182px; top: 266px; transform: translateY(-48px); color: var(--ink); }
  .card--back .tagline { left: 220px; top: 312px; color: var(--white); }

  .person { position: absolute; right: 604px; top: 46px; text-align: right; font-family: "Source Sans 3", sans-serif; color: var(--ink); }
  .person__name { font-size: 47px; line-height: 1; }
  .person__role { font-size: 40px; line-height: .9; }
  .divider { position: absolute; left: 337px; top: 22px; width: 4px; height: 171px; background: var(--ink); }

  .contacts { position: absolute; left: 366px; top: 30px; list-style: none; font-family: "Source Sans 3", sans-serif; font-size: 27px; color: var(--ink); }
  .contacts li { display: flex; align-items: center; height: 33.5px; white-space: nowrap; }
  .contacts svg { width: 19px; height: 19px; margin-right: 20px; flex: none; }
</style>
</head>
<body>
  <section class="card card--front">
    <div class="front-top"></div>
    <div class="front-rule"></div>
    <div class="wordmark">vorp</div>
    <span class="mark-dot"></span>
    <p class="tagline">a Qorvel Media incubator</p>
    <div class="front-info">
      <div class="person">
        <p class="person__name">dale fenwright</p>
        <p class="person__role">ceo</p>
      </div>
      <span class="divider"></span>
      <ul class="contacts">
        <li><svg viewBox="0 0 20 20"><rect width="20" height="20" fill="#111"/><path d="M6 4l3 3-2 2q2 3 4 4l2-2 3 3-2 2Q8 16 4 6z" fill="#229d71"/></svg>555 247 3318</li>
        <li><svg viewBox="0 0 20 20"><rect width="20" height="20" fill="#111"/><rect x="6" y="3" width="8" height="14" rx="1" fill="#229d71"/><rect x="7.5" y="5" width="5" height="5" fill="#111"/></svg>555 738 1194</li>
        <li><svg viewBox="0 0 20 20"><rect width="20" height="20" fill="#111"/><rect x="3" y="6" width="14" height="9" fill="#229d71"/><path d="M3 6l7 5 7-5" stroke="#111" stroke-width="1.3" fill="none"/></svg>dale.fenwright@vorp.example</li>
        <li><svg viewBox="0 0 20 20"><rect width="20" height="20" fill="#111"/><circle cx="10" cy="10" r="6" fill="none" stroke="#229d71" stroke-width="1.6"/><path d="M4 10h12M10 4q-3 6 0 12M10 4q3 6 0 12" stroke="#229d71" stroke-width="1.2" fill="none"/></svg>www.vorp.example</li>
        <li><svg viewBox="0 0 20 20"><rect width="20" height="20" fill="#111"/><path d="M3 10l7-6 7 6h-2v6h-4v-4H9v4H5v-6z" fill="#229d71"/></svg>218 9th avenue 3rd floor lindenport ca 95555</li>
      </ul>
    </div>
  </section>

  <section class="card card--back">
    <div class="wordmark">vorp</div>
    <span class="mark-dot"></span>
    <p class="tagline">a Qorvel Media incubator</p>
  </section>
</body>
</html>
```